Brindlewick Music Studio needs a promotional postcard design

We are looking for a postcard design for a small business that provides clients with private music lesson instruction. We are looking for a design that will convey the message of "music is fun for kids" that will appeal to parents and encourage them to sign up. We have a company logo that should be used and our color scheme is teal and turquoise. All of our contact info should be displayed as well.

Target Market(s)

Parents with young kids

Contact Information for Business Card

web: www.brindlewickmusicstudio.example
email: lessons@brindlewickmusicstudio.example
phone: 202-555-0147

Font styles to use
Serif
Sans Serif

Colors
33b8a4
86cfc6
0456a4
87cfc6

Requirements
Must have
• Music lessons in your home
• Creating little stars one at a time
• Sign Up Now
• Please use these images:
Nice to have
• Something like this sample postcard:

```html
<!DOCTYPE html>
<html lang="en">
<head>
<meta charset="utf-8">
<title>Brindlewick Music Studio – Card</title>
<link rel="stylesheet" href="https://fonts.googleapis.com/css2?family=Poiret+One&family=Open+Sans:wght@700&display=swap">
<style>
  :root {
    --teal: #2fc3bd;
    --teal-light: #3fcfc8;
    --teal-deep: #24b3ad;
    --logo-teal: #4fb7bc;
    --badge-grey: #6e6e6e;
    --ink: #1f2230;
    --paper: #ffffff;
    --edge: #e4e4e4;
  }
  html, body {
    margin: 0;
    padding: 0;
    width: 1200px;
    height: 1200px;
    overflow: hidden;
    background: var(--paper);
  }
  .canvas {
    position: relative;
    width: 1200px;
    height: 1200px;
  }
  .card {
    position: absolute;
    left: 215px;
    width: 804px;
    height: 447px;
    background: var(--paper);
    overflow: hidden;
    box-sizing: border-box;
    border: 1px solid var(--edge);
  }
  .card--front { top: 93px; }
  .card--back { top: 590px; }

  .pattern {
    position: absolute;
    left: 0;
    top: 0;
    width: 100%;
    background: radial-gradient(ellipse at 50% 50%, var(--teal-light) 0%, var(--teal) 55%, var(--teal-deep) 100%);
  }
  .card--front .pattern { height: 395px; }
  .card--back .pattern { height: 150px; }

  .brand-badge {
    position: absolute;
    left: 298px;
    top: 83px;
    width: 206px;
    height: 206px;
    border-radius: 50%;
    background: var(--paper);
    display: flex;
    align-items: center;
    justify-content: center;
    text-align: center;
  }
  .brand-badge__name {
    font-family: "Poiret One", sans-serif;
    font-size: 26px;
    line-height: 1.2;
    color: var(--logo-teal);
    padding: 0 20px;
  }

  .studio-name {
    position: absolute;
    left: 0;
    right: 0;
    top: 395px;
    height: 52px;
    margin: 0;
    font-family: "Poiret One", sans-serif;
    font-weight: 400;
    font-size: 38px;
    line-height: 52px;
    text-align: center;
    color: #111;
  }

  .tagline {
    position: absolute;
    left: 280px;
    top: -68px;
    width: 244px;
    height: 244px;
    border-radius: 50%;
    background: var(--badge-grey);
    color: #f2f2f2;
    font-family: "Poiret One", sans-serif;
    text-align: center;
  }
  .tagline__text {
    position: absolute;
    left: 0;
    right: 0;
    top: 76px;
    margin: 0;
    font-size: 27px;
    line-height: 40px;
  }
  .tagline__accent {
    display: block;
    font-size: 36px;
    line-height: 52px;
  }

  .contact-list {
    position: absolute;
    left: 150px;
    top: 248px;
    margin: 0;
    padding: 0;
    list-style: none;
  }
  .contact-list__item {
    display: flex;
    align-items: center;
    height: 54px;
    font-family: "Open Sans", sans-serif;
    font-weight: 700;
    font-size: 19px;
    letter-spacing: 1.6px;
    color: var(--ink);
  }
  .contact-list__icon {
    width: 36px;
    height: 36px;
    margin-right: 36px;
    flex: none;
  }
</style>
</head>
<body>
<main class="canvas">

  <section class="card card--front">
    <div class="pattern" role="img" aria-label="Turquoise background with a hand-drawn pattern of guitars, microphones, keyboards, drums, speakers and music notes"></div>
    <div class="brand-badge">
      <span class="brand-badge__name">Brindlewick</span>
    </div>
    <h1 class="studio-name">Brindlewick Music Studio</h1>
  </section>

  <section class="card card--back">
    <div class="pattern" role="img" aria-label="Turquoise band with a hand-drawn pattern of guitars, microphones, keyboards and music notes"></div>
    <div class="tagline">
      <p class="tagline__text">Music<br>lessons for kids<br>are<span class="tagline__accent">fun</span></p>
    </div>

    <ul class="contact-list">
      <li class="contact-list__item">
        <svg class="contact-list__icon" viewBox="0 0 36 36" aria-hidden="true">
          <path fill="var(--ink)" d="M8 3c1.6-.8 3-.4 3.8 1l3 5.2c.7 1.3.3 2.6-.8 3.4l-2 1.4c1.4 3.6 4.4 7.6 7.6 10l2-1.3c1.1-.7 2.5-.5 3.3.6l3.6 4.6c.9 1.2.6 2.8-.6 3.6l-2.2 1.5c-2 1.3-4.8 1.2-7-.4C11.6 27.8 6 20.6 4.2 13 3.6 10.4 4.4 7.6 6.3 6L8 3z"/>
        </svg>
        <span>202-555-0147</span>
      </li>
      <li class="contact-list__item">
        <svg class="contact-list__icon" viewBox="0 0 36 36" aria-hidden="true">
          <rect x="1" y="7" width="34" height="22" fill="var(--ink)"/>
          <path d="M2 8 L18 20 L34 8" fill="none" stroke="#fff" stroke-width="2.2"/>
        </svg>
        <span>LESSONS@BRINDLEWICKMUSICSTUDIO.EXAMPLE</span>
      </li>
      <li class="contact-list__item">
        <svg class="contact-list__icon" viewBox="0 0 36 36" aria-hidden="true">
          <circle cx="18" cy="18" r="16" fill="var(--ink)"/>
          <g fill="none" stroke="#fff" stroke-width="1.8">
            <ellipse cx="18" cy="18" rx="7" ry="16"/>
            <line x1="18" y1="2" x2="18" y2="34"/>
            <line x1="2" y1="18" x2="34" y2="18"/>
            <path d="M5 10 H31 M5 26 H31"/>
          </g>
        </svg>
        <span>WWW.BRINDLEWICKMUSICSTUDIO.EXAMPLE</span>
      </li>
    </ul>
  </section>

</main>
</body>
</html>
```